New bussiness card, using company logo.
Lachlan Voss
Manager/Director
Birch Property Developments
Po Box 4657
Carraway Central
Qld
0455 386 218
lachlan@birchpropertydevelopments
eye catching, vibrant colours, professional

```html
<!DOCTYPE html>
<html lang="en">
<head>
<meta charset="utf-8">
<title>Birch Property Developments – Business Card</title>
<link href="https://fonts.googleapis.com/css2?family=Titillium+Web:wght@400;600;700&display=swap" rel="stylesheet">
<style>
  :root {
    --page-bg: #f2f3f3;
    --card-white: #ffffff;
    --brand-red: #e0262b;
    --brand-green: #4cb848;
    --green-light: #a6d13a;
    --green-mid: #77c043;
    --text-grey: #646566;
    --text-white: #ffffff;
  }
  * { margin: 0; padding: 0; box-sizing: border-box; }
  html, body {
    width: 1200px; height: 1000px; overflow: hidden;
    background: var(--page-bg);
    font-family: "Titillium Web", sans-serif;
  }
  .canvas { position: relative; width: 1200px; height: 1000px; }

  .card {
    position: absolute; left: 281px; width: 638px; height: 390px;
    overflow: hidden;
  }
  .card--front { top: 97px; background: var(--card-white); }
  .card--back {
    top: 520px;
    background: radial-gradient(ellipse at 85% 10%, var(--green-light) 0%, var(--green-mid) 50%, var(--brand-green) 100%);
  }
  .card__band {
    position: absolute; left: 0; bottom: 0; width: 100%; height: 14px;
    background: var(--brand-red);
  }

  .wordmark {
    position: absolute; display: flex; align-items: center; gap: 14px;
    font-weight: 700; text-transform: uppercase; line-height: 1.05;
  }
  .wordmark__square { width: 34px; height: 34px; flex: none; }
  .wordmark__name { font-size: 30px; letter-spacing: 0.5px; }

  .card--front .wordmark { left: 40px; top: 104px; color: var(--brand-red); }
  .card--front .wordmark__square { background: var(--brand-green); }
  .card--back .wordmark { left: 0; width: 100%; top: 162px; justify-content: center; color: var(--text-white); }
  .card--back .wordmark__square { background: var(--text-white); }

  .contact {
    position: absolute; left: 39px; top: 246px; color: var(--text-grey);
  }
  .contact__name { font-size: 18px; font-weight: 700; letter-spacing: 0.5px; line-height: 22px; }
  .contact__role { font-size: 18px; line-height: 24px; letter-spacing: 0.2px; }
  .contact__lines { margin-top: 16px; list-style: none; }
  .contact__line { display: flex; align-items: center; gap: 6px; font-size: 18px; line-height: 22px; letter-spacing: 0.2px; }
  .contact__line--phone { font-size: 16px; font-weight: 600; letter-spacing: 1px; }
  .contact__icon {
    width: 20px; height: 20px; border-radius: 50%; flex: none;
    background: radial-gradient(circle at 40% 30%, var(--green-light), var(--brand-green));
    color: var(--text-white); font-size: 13px; font-weight: 700; letter-spacing: 0;
    display: flex; align-items: center; justify-content: center;
  }

  .address {
    position: absolute; left: 423px; top: 242px; color: var(--text-grey);
    font-size: 18px; line-height: 22.5px; font-style: normal; letter-spacing: 0.4px;
  }
  .address__company { font-weight: 700; letter-spacing: 0.5px; text-transform: uppercase; }
</style>
</head>
<body>
<main class="canvas">
  <section class="card card--front" aria-label="Business card front">
    <div class="wordmark">
      <span class="wordmark__square"></span>
      <span class="wordmark__name">Birch Property<br>Developments</span>
    </div>

    <div class="contact">
      <p class="contact__name">LACHLAN VOSS</p>
      <p class="contact__role">Manager/Director</p>
      <ul class="contact__lines">
        <li class="contact__line contact__line--phone"><span class="contact__icon">T</span>0455 386 218</li>
        <li class="contact__line"><span class="contact__icon">E</span>lachlan@birchpropertydevelopments</li>
      </ul>
    </div>

    <address class="address">
      <p class="address__company">Birch Property<br>Developments</p>
      <p>P.O. Box 4657<br>Carraway Central<br>Northshire</p>
    </address>

    <div class="card__band"></div>
  </section>

  <section class="card card--back" aria-label="Business card back">
    <div class="wordmark">
      <span class="wordmark__square"></span>
      <span class="wordmark__name">Birch Property<br>Developments</span>
    </div>
    <div class="card__band"></div>
  </section>
</main>
</body>
</html>
```